Geschäftspapiere Campingplatz
Zielgruppe
Campingplatz
Aufgabenstellung
Geschäftspapiere, Briefpapier, Visitenkarte, Briefumschlag und DIN A5 Memoblock farblich und designmäßig am Logo orientiert.
Memoblock sollte sich vom Briefpapier unterscheiden und nicht so viele Daten enthalten.
Website, E-Mail, Telefonnummer, Festnetz, Adresse und Inhaber sollen auf dem Briefpapier erscheinen.
Auf der Visitenkarte soll nur statt Inhaber stehen und zusätzlich die Handynummer, sowie alle anderen Daten.
Die Datensätze sollten sich mit entsprechendem Programm von uns bearbeiten lassen.

```html
<!DOCTYPE html>
<html lang="de">
<head>
<meta charset="utf-8">
<title>Camping Lindenau – Geschäftspapiere</title>
<link href="https://fonts.googleapis.com/css2?family=Open+Sans:wght@400;600;700&display=swap" rel="stylesheet">
<style>
  :root {
    --backdrop: #e6e9ec;
    --paper: #ffffff;
    --band: #7b9a4b;
    --rule: #7aa03c;
    --brand: #8c8a2c;
    --ink: #3a3a3a;
    --muted: #8a8a8a;
    --on-band: #f4f7ee;
  }
  * { margin: 0; padding: 0; box-sizing: border-box; }
  html, body { width: 1200px; height: 800px; overflow: hidden; }
  body {
    background: var(--backdrop);
    font-family: "Open Sans", Arial, sans-serif;
    color: var(--ink);
    position: relative;
  }
  .sheet {
    position: absolute;
    top: 40px;
    width: 510px;
    height: 720px;
    background: var(--paper);
    box-shadow: 0 2px 10px rgba(0,0,0,0.12);
    overflow: hidden;
  }
  .memo { left: 60px; }
  .letter { left: 630px; }

  .brand {
    position: absolute;
    left: 0; right: 0;
    text-align: center;
    font-weight: 700;
    color: var(--brand);
  }
  .memo .brand { top: 44px; font-size: 24px; }
  .letter .brand { top: 34px; font-size: 18px; }
  .brand-dot {
    display: inline-block;
    width: 10px; height: 10px;
    border-radius: 50%;
    background: var(--brand);
    margin-right: 8px;
    vertical-align: middle;
  }

  .memo-rule {
    position: absolute;
    left: 50px; right: 50px;
    top: 98px;
    height: 2px;
    background: var(--rule);
  }

  .footer-band {
    position: absolute;
    left: 0; right: 0; bottom: 0;
    background: var(--band);
    color: var(--on-band);
    display: flex;
    justify-content: space-between;
  }
  .memo .footer-band { height: 112px; padding: 22px 40px; font-size: 13px; letter-spacing: 0.06em; }
  .letter .footer-band { height: 80px; padding: 16px 44px; font-size: 9px; }
  .footer-name { font-weight: 600; margin-bottom: 8px; }
  .footer-contact { text-align: right; line-height: 1.5; }
  .memo .footer-contact .footer-email { margin-bottom: 10px; }
  .footer-address { line-height: 1.45; }

  .sender-line {
    position: absolute;
    left: 70px; top: 96px;
    width: 230px;
    font-size: 7px;
    color: var(--muted);
    border-bottom: 1px solid var(--muted);
    padding-bottom: 3px;
  }
  .address-zone {
    position: absolute;
    left: 70px; top: 132px;
    font-size: 8px;
    color: var(--ink);
  }
  .letter-body {
    position: absolute;
    left: 70px; right: 56px;
    top: 250px;
    font-size: 8.5px;
    line-height: 1.5;
  }
  .letter-body p { margin-bottom: 10px; }
  .closing { margin-top: 40px; }
  .signature { margin-top: 16px; }
</style>
</head>
<body>

  <section class="sheet memo" aria-label="Memoblock">
    <div class="brand"><span class="brand-dot"></span>Camping Lindenau</div>
    <div class="memo-rule"></div>
    <footer class="footer-band">
      <div>
        <div class="footer-name">Camping Lindenau</div>
        <div class="footer-address">Lindenweg 12<br>54321 Talbach</div>
      </div>
      <div class="footer-contact">
        <div class="footer-email">info@camping-lindenau.de</div>
        <div>www.camping-lindenau.de</div>
        <div>Telefon: +49 1234 567890</div>
        <div>Telefax: +49 1234 567891</div>
      </div>
    </footer>
  </section>

  <section class="sheet letter" aria-label="Briefpapier">
    <div class="brand"><span class="brand-dot"></span>Camping Lindenau</div>
    <div class="sender-line">Marlene Vogt, Lindenweg 12, 54321 Talbach</div>
    <div class="address-zone">Anschriftzone</div>
    <div class="letter-body">
      <p>Sehr geehrte Damen und Herren,</p>
      <p>vielen Dank für Ihre Anfrage zu unserem Campingplatz. Gerne bestätigen wir Ihnen die Reservierung eines Stellplatzes für den gewünschten Zeitraum. Der Platz liegt ruhig am Waldrand, Strom und Wasser sind direkt vorhanden. Die Anreise ist ab vierzehn Uhr möglich, die Abreise bis elf Uhr.</p>
      <p>Bitte bringen Sie bei der Ankunft diese Bestätigung mit. Brötchen können Sie am Vorabend an der Rezeption bestellen. Haustiere sind nach Absprache willkommen.</p>
      <p>Wir freuen uns auf Ihren Besuch und wünschen Ihnen eine gute Anreise.</p>
      <p class="closing">Mit freundlichen Grüßen,</p>
      <p class="signature">Marlene Vogt</p>
    </div>
    <footer class="footer-band">
      <div>
        <div class="footer-name">Camping Lindenau</div>
        <div class="footer-address">Inhaberin: Marlene Vogt<br>Lindenweg 12<br>54321 Talbach</div>
      </div>
      <div class="footer-contact">
        <div>info@camping-lindenau.de</div>
        <div>www.camping-lindenau.de</div>
        <div>Telefon: +49 1234 567890</div>
        <div>Telefax: +49 1234 567891</div>
      </div>
    </footer>
  </section>

</body>
</html>
```